Iconset für Bestellablauf eines Fensterlieferanten/Produzenten
Zielgruppe
Guten Tag,
wir sind Fenster Hersteller und Produzent von edlen Aluminiumfenstern basierend auf Venrak Profilen. Unsere Qualität der Produkte, unser Service und Zuverlässigkeit stehen dabei an oberster Stelle.
Aufgabenstellung
Wir suchen ein Iconset für eine Auflistung aller Punkte unseres Bestellablaufes. Dieser Bestellablauf ist auf folgender Webseite zu sehen: http://www.rahmenwerk17.example/bestellablauf
Designlich sollte es auch zu folgender Webseite passen: http://www.glaspanel17.example/
Es sind neun Punkte, die jeweils ein schönes Icon benötigen, in dem oben angegebenem Link können Sie die Tätigkeiten der jeweiligen Punkte einsehen. Diesen Tätigkeiten sollte jedes Icon natürlich entsprechen.
Wir sind gespannt auf Ihre Vorschläge!

```html
<!DOCTYPE html>
<html lang="de">
<head>
<meta charset="utf-8">
<title>Rahmenwerk17 – Bestellablauf</title>
<link rel="stylesheet" href="https://fonts.googleapis.com/css2?family=Arimo:wght@400;700&family=Open+Sans:wght@400;600&display=swap">
<style>
  :root {
    --ink: #1c1c1c;
    --muted: #333;
    --brand: #1c5fa8;
    --brand-dark: #173c6d;
    --icon: #1d63ad;
    --rule: #d4d4d4;
    --nav: #1a1a1a;
    --badge: #4a4d52;
    --bg-fade: #e6e6e6;
  }
  * { box-sizing: border-box; margin: 0; padding: 0; }
  html, body { width: 848px; height: 1200px; overflow: hidden; }
  body {
    position: relative;
    font-family: "Arimo", Arial, sans-serif;
    color: var(--ink);
    background: linear-gradient(90deg, #fff 0%, #fff 70%, var(--bg-fade) 100%);
  }
  .site-header { position: absolute; left: 0; top: 0; width: 848px; height: 135px;
    background: linear-gradient(90deg, #fff 0%, #fff 55%, #e4e4e4 100%); }
  .brand { position: absolute; left: 57px; top: 70px; display: flex; align-items: center; gap: 10px; }
  .brand-mark { width: 26px; height: 26px; background: var(--brand-dark); }
  .brand-name { font-family: "Arimo", Arial, sans-serif; font-size: 31px; font-weight: 400; color: var(--brand-dark); letter-spacing: -0.5px; }

  .hero { position: absolute; left: 0; top: 135px; width: 848px; height: 232px;
    background: linear-gradient(90deg, #6f7479 0%, #c9cbcc 25%, #e9e9e9 45%, #8d8f90 62%, #3a4048 78%, #6f7d8c 100%); }

  .main-nav { position: absolute; left: 24px; top: 291px; width: 830px; height: 36px;
    border: 1px solid #fff; background: rgba(20,20,20,.85); }
  .main-nav a { position: absolute; top: 10px; font-size: 11px; font-weight: 700; color: #fff; text-decoration: none; letter-spacing: .1px; }
  .nav-second { position: absolute; left: 34px; top: 339px; font-size: 11px; font-weight: 700; color: #fff; }

  .sidebar { position: absolute; left: 11px; top: 398px; width: 180px; }
  .sidebar h2 { font-family: "Open Sans", Arial, sans-serif; font-weight: 400; font-size: 18px; color: var(--brand); margin-bottom: 20px; }
  .page-list { list-style: none; }
  .page-list li { font-size: 12.5px; color: var(--muted); height: 24px; line-height: 20px; padding-left: 5px; }
  .page-list li.current { background: var(--brand-dark); color: #fff; font-weight: 700; width: 86px; }
  .partner { margin-top: 50px; display: flex; align-items: center; gap: 8px; }
  .partner-square { width: 20px; height: 20px; background: var(--badge); }
  .partner-name { font-size: 20px; color: var(--badge); font-weight: 400; letter-spacing: 1px; }
  .partner-link { margin-top: 28px; font-size: 12px; color: var(--muted); display: flex; align-items: center; gap: 5px; }
  .pdf-tag { width: 14px; height: 9px; background: #d33; border-radius: 1px; }

  .content { position: absolute; left: 214px; top: 396px; width: 634px; overflow: hidden; }
  .content h1 { font-family: "Open Sans", Arial, sans-serif; font-weight: 400; font-size: 21px; color: var(--ink);
    padding-bottom: 8px; border-bottom: 1px solid var(--rule); }
  .content h2 { font-family: "Open Sans", Arial, sans-serif; font-weight: 400; font-size: 19.5px; color: var(--ink);
    margin-top: 12px; white-space: nowrap; }
  .intro { margin-top: 8px; font-size: 12px; line-height: 18px; color: var(--muted); white-space: nowrap; }

  .steps { position: absolute; left: 214px; top: 555px; width: 634px; list-style: none; overflow: hidden; }
  .step { position: relative; height: 67px; border-bottom: 1px solid var(--rule); }
  .step:last-child { border-bottom: 0; }
  .step-icon { position: absolute; left: 0; top: 6px; width: 36px; height: 44px; }
  .step-text { position: absolute; left: 52px; top: 6px; font-size: 12px; line-height: 19px; color: var(--muted); white-space: nowrap; }
</style>
</head>
<body>
  <header class="site-header">
    <div class="brand"><span class="brand-mark"></span><span class="brand-name">Rahmenwerk17</span></div>
  </header>

  <div class="hero" role="img" aria-label="Fotostreifen mit moderner Architektur, großen Alu-Fensterfronten und Innenraum"></div>

  <nav class="main-nav">
    <a style="left:9px">HOME</a>
    <a style="left:66px">ALUMINIUMFENSTER</a>
    <a style="left:209px">PREISLISTEN</a>
    <a style="left:302px">REFERENZEN</a>
    <a style="left:404px">MONTAGE</a>
    <a style="left:485px">PARTNER</a>
    <a style="left:563px">SERVICE</a>
    <a style="left:634px">UNTERNEHMEN</a>
    <a style="left:746px">STANDORTE</a>
  </nav>
  <div class="nav-second">KONTAKT</div>

  <aside class="sidebar">
    <h2>Seiten</h2>
    <ul class="page-list">
      <li>Home</li><li>Aluminiumfenster</li><li>Preislisten</li><li>Referenzen</li>
      <li>Montage</li><li>Partner</li><li>Service</li><li>Unternehmen</li>
      <li>Standorte</li><li class="current">Bestellablauf</li><li>Kontakt</li>
    </ul>
    <div class="partner"><span class="partner-square"></span><span class="partner-name">VENRAK</span></div>
    <div class="partner-link">Venrak Alu Fenster <span class="pdf-tag"></span></div>
  </aside>

  <main class="content">
    <h1>Bestellablauf eines Auftrages</h1>
    <h2>Rahmenwerk 17 setzt in Sachen Preis/Leistung und Servicequalität neue Maßstäbe</h2>
    <p class="intro">Das bedeutet für uns vor allem kompetente Beratung und Bearbeitung Ihrer Bestellung. Aus diesem Grund verbinden wir<br>Serviceleistungen, damit wir Ihnen einen angenehmen und reibungslosen Bestellablauf anbieten können. Daher stellen wir<br>Bestellablaufprozess in einzelnen Punkten vor.</p>
  </main>

  <ol class="steps">
    <li class="step">
      <svg class="step-icon" viewBox="0 0 36 44"><rect y="4" width="36" height="36" rx="4" fill="var(--icon)"/><path d="M9 20v12h14" fill="none" stroke="#fff" stroke-width="2.5"/><path d="M14 26l12-12 4 4-12 12h-4z" fill="#fff"/></svg>
      <p class="step-text">Stellen Sie uns einfach eine Anfrage zu Ihrem Anliegen an Rahmenwerk17 mit den dazugehörigen Unterlagen oder<br>senden uns einfach die CAD oder Architektur-Zeichnung zu.</p>
    </li>
    <li class="step">
      <svg class="step-icon" viewBox="0 0 36 44"><rect y="4" width="36" height="36" rx="4" fill="var(--icon)"/><circle cx="18" cy="22" r="10" fill="none" stroke="#fff" stroke-width="2.5"/><path d="M18 16v6h5" fill="none" stroke="#fff" stroke-width="2.5"/></svg>
      <p class="step-text">Wir erarbeiten Ihr Angebot zu Aluminium Elementen in möglichst kurzer Zeit und prüfen Ihre Anfrage. Falls<br>spezieller Absprachebedarf existieren, so kontaktieren wir Sie und bieten Ihnen Vorschläge zur Verbesserung. Nach<br>ausgiebiger Prüfung Ihrer Anfrage lassen wir Ihnen ein Angebot zukommen.</p>
    </li>
    <li class="step">
      <svg class="step-icon" viewBox="0 0 36 44"><rect y="4" width="36" height="36" rx="4" fill="var(--icon)"/><path d="M8 16h20v14H8z" fill="none" stroke="#fff" stroke-width="2.2"/><path d="M8 16l10 8 10-8" fill="none" stroke="#fff" stroke-width="2.2"/><path d="M6 30l7-6" stroke="#fff" stroke-width="2"/></svg>
      <p class="step-text">Wenn Ihnen die Konditionen und die Zusammenarbeit von Rahmenwerk17 zusagt, setzen Sie sich mit uns in Verbindung, damit wir<br>dem Bestellablauf fortfahren können.</p>
    </li>
    <li class="step">
      <svg class="step-icon" viewBox="0 0 36 44"><rect y="4" width="36" height="36" rx="4" fill="var(--icon)"/><circle cx="13" cy="16" r="4" fill="#fff"/><circle cx="24" cy="16" r="4" fill="#fff"/><path d="M6 32c0-6 3-9 7-9s7 3 7 9zM17 32c0-6 3-9 7-9s7 3 7 9z" fill="#fff"/></svg>
      <p class="step-text">Ein Außendienstmitarbeiter kommt auf Wunsch bei Ihnen vorbei um technische Details Ihrer Anfrage zu klären und<br>um Sie bestmöglich über unsere Aluminiumprofile und Materialien zu unterstützen und zu beraten.</p>
    </li>
    <li class="step">
      <svg class="step-icon" viewBox="0 0 36 44"><rect y="4" width="36" height="36" rx="4" fill="var(--icon)"/><circle cx="14" cy="26" r="5" fill="none" stroke="#fff" stroke-width="2.5"/><path d="M14 18v3M14 31v3M6 26h3M19 26h3" stroke="#fff" stroke-width="2.5"/><circle cx="25" cy="14" r="4" fill="#fff"/></svg>
      <p class="step-text">Nachdem Sie uns einen Auftrag zur Aluminiumfenster Produktion erteilt haben, wird nach einer Terminabsprache das<br>Feinaufmaß an Ihrem Bauvorhaben durchgeführt.</p>
    </li>
    <li class="step">
      <svg class="step-icon" viewBox="0 0 36 44"><rect y="4" width="36" height="36" rx="4" fill="var(--icon)"/><rect x="8" y="12" width="20" height="20" rx="2" fill="none" stroke="#fff" stroke-width="2.2"/><path d="M8 17h20M13 9v5M23 9v5" stroke="#fff" stroke-width="2.2"/><text x="18" y="29" font-size="9" font-weight="700" fill="#fff" text-anchor="middle" font-family="Arimo, sans-serif">31</text></svg>
      <p class="step-text">Nach Festlegung aller technischen Details und Konditionen beginnt die Fertigung der von Ihnen bestellten Fenster. Die Dauer<br>der Fertigung beträgt je nach Umfang 6 bis 8 Wochen.</p>
    </li>
    <li class="step">
      <svg class="step-icon" viewBox="0 0 36 44"><rect y="4" width="36" height="36" rx="4" fill="var(--icon)"/><circle cx="22" cy="16" r="5" fill="none" stroke="#fff" stroke-width="2.5"/><path d="M22 21l-4 6-7 3" fill="none" stroke="#fff" stroke-width="2.5"/><circle cx="11" cy="30" r="2.5" fill="#fff"/></svg>
      <p class="step-text">Ihre Ware verlässt mit dem dienstseigenen LKW unsere Rahmenwerk17 Produktionsstätte und wird am Bestimmungsort an Ihre<br>vorgegebene Lieferadresse angeliefert. Den Liefertermin für die Fenster bestimmen natürlich Sie.</p>
    </li>
    <li class="step">
      <svg class="step-icon" viewBox="0 0 36 44"><rect y="4" width="36" height="36" rx="4" fill="var(--icon)"/><rect x="13" y="14" width="15" height="15" fill="none" stroke="#fff" stroke-width="2.2"/><path d="M20.5 14v15M13 21.5h15" stroke="#fff" stroke-width="2"/><path d="M6 21.5h5M9 19l2.5 2.5L9 24" fill="none" stroke="#fff" stroke-width="2"/></svg>
      <p class="step-text">Bei hinzugebuchter Montageleistung erfolgt im Anschluss der Lieferung die Montage. Unsere Hausmonteure<br>übernehmen gerne diese Arbeit für Sie. Der Termin wird mit Ihnen telefonisch festgelegt.</p>
    </li>
    <li class="step">
      <svg class="step-icon" viewBox="0 0 36 44"><rect y="4" width="36" height="36" rx="4" fill="var(--icon)"/><circle cx="16" cy="16" r="4.5" fill="#fff"/><path d="M7 34c0-7 4-11 9-11s9 4 9 11z" fill="#fff"/><circle cx="26" cy="13" r="5" fill="var(--icon)" stroke="#fff" stroke-width="1.8"/><path d="M23.5 13l2 2 3-3.5" fill="none" stroke="#fff" stroke-width="1.6"/></svg>
      <p class="step-text">Nach Abschluss aller ausgeführten Aufgaben, der Fensterproduktion, Lieferung und gegebenenfalls der Montage ist das Projekt<br>fertiggestellt. Nach der Fertigstellung erhalten Sie einen umfassenden Zugang zu unserem After Sales Service, der Ihnen bei<br>Rahmenwerk17 beratend zur Seite steht.</p>
    </li>
  </ol>
</body>
</html>
```